I need a business card for my new bakery - Mill Lane Oven Co. We make biscuits, cakes, muffins and other sweets. Our food is honest, wholesome and down to earth - i'd love this to be reflected in the design of the card. The design MUST include our logo (see the attached image - which needs to be replicated). The design should only use 2 or at most 3 colours.

Industry/Entity Type

Bakery

Requirements
Must have
• Must include my logo.
Must have a clean, simple design.
Space for my name, my title, my phone number, my facebook page (I will provide details later)
Should not have
• Must not have lots of bright colours.
Must not have any unnescassry graphics.

```html
<!DOCTYPE html>
<html lang="en">
<head>
<meta charset="utf-8">
<title>Mill Lane Oven Co – Business Card</title>
<link rel="stylesheet" href="https://fonts.googleapis.com/css2?family=Barlow+Condensed:ital,wght@0,700;1,500&family=Damion&display=swap">
<style>
  :root {
    --ink: #0b0b0b;
    --board: #4a4442;
    --gold: #c9a26b;
    --gold-light: #f3e3c2;
    --gold-dark: #8a6a3d;
    --script: "Damion", cursive;
    --display: "Barlow Condensed", sans-serif;
  }
  html, body {
    margin: 0;
    padding: 0;
    overflow: hidden;
    background: #ffffff;
  }
  .card {
    position: relative;
    width: 1200px;
    height: 730px;
    background: var(--board);
    overflow: hidden;
  }
  .card__shapes {
    position: absolute;
    inset: 0;
  }
  .brand {
    position: absolute;
    left: 40px;
    top: 48px;
    display: flex;
    align-items: center;
    gap: 18px;
  }
  .brand__mark {
    width: 34px;
    height: 34px;
    background: var(--gold);
  }
  .brand__name {
    font-family: var(--display);
    font-weight: 700;
    font-size: 64px;
    line-height: 1;
    color: var(--gold);
    letter-spacing: 1px;
  }
  .headline {
    position: absolute;
    right: 58px;
    top: 14px;
    margin: 0;
    font-family: var(--display);
    font-style: italic;
    font-weight: 500;
    font-size: 112px;
    line-height: 1;
    color: var(--gold);
    letter-spacing: 2px;
  }
  .offer {
    position: absolute;
    right: 18px;
    top: 228px;
    text-align: right;
    font-family: var(--script);
    color: var(--gold);
  }
  .offer__title {
    margin: 0;
    font-size: 50px;
    font-weight: 400;
    line-height: 1;
  }
  .offer__list {
    list-style: none;
    margin: 14px 0 0;
    padding: 0;
    width: 250px;
    margin-left: auto;
    margin-right: 40px;
    text-align: left;
    font-size: 38px;
    line-height: 47px;
  }
  .tagline {
    position: absolute;
    left: 680px;
    top: 525px;
    width: 520px;
    margin: 0;
    text-align: center;
    font-family: var(--script);
    font-size: 34px;
    line-height: 40px;
    color: var(--gold);
    letter-spacing: 1px;
  }
  .contact {
    position: absolute;
    left: 60px;
    top: 378px;
    margin: 0;
    font-family: var(--script);
    font-size: 46px;
    color: var(--gold);
  }
  .contact dt { display: none; }
  .contact dd {
    margin: 0;
    line-height: 1;
  }
  .contact__name { height: 68px; }
  .contact__title { height: 78px; }
  .contact__phone { height: 92px; }
</style>
</head>
<body>
<main class="card">
  <svg class="card__shapes" width="1200" height="730" viewBox="0 0 1200 730" aria-hidden="true">
    <defs>
      <linearGradient id="ribbon" x1="0" y1="0" x2="1" y2="0">
        <stop offset="0" stop-color="var(--gold-dark)"/>
        <stop offset="0.35" stop-color="var(--gold-light)"/>
        <stop offset="0.6" stop-color="var(--gold)"/>
        <stop offset="0.85" stop-color="var(--gold-light)"/>
        <stop offset="1" stop-color="var(--gold-dark)"/>
      </linearGradient>
    </defs>
    <!-- top band -->
    <path class="band-top" d="M0 0 H1200 V120 C950 128 720 190 480 255 C320 298 160 318 0 314 Z" fill="var(--ink)"/>
    <path class="ribbon-top" d="M0 314 C160 318 320 298 480 255 C720 190 950 128 1200 120 V144 C950 150 720 212 480 276 C320 318 160 330 0 326 Z" fill="url(#ribbon)"/>
    <!-- bottom corner band -->
    <path class="band-bottom" d="M560 730 C760 655 980 628 1200 636 V730 Z" fill="var(--ink)"/>
    <path class="ribbon-bottom" d="M560 730 C760 655 980 628 1200 636 V654 C980 648 780 672 600 730 Z" fill="url(#ribbon)"/>
  </svg>

  <div class="brand">
    <span class="brand__mark"></span>
    <span class="brand__name">MILL LANE</span>
  </div>

  <h1 class="headline">OVEN CO.</h1>

  <section class="offer">
    <h2 class="offer__title">Available Things.</h2>
    <ul class="offer__list">
      <li>Biscuits</li>
      <li>Cakes</li>
      <li>Muffins</li>
      <li>Sweets.</li>
    </ul>
  </section>

  <p class="tagline">Our food is honest<br>wholesome and down to earth.</p>

  <dl class="contact">
    <dt>Name</dt><dd class="contact__name">Name Here</dd>
    <dt>Title</dt><dd class="contact__title">Title</dd>
    <dt>Phone</dt><dd class="contact__phone">Phone No.</dd>
    <dt>Facebook</dt><dd class="contact__social">Facebook:</dd>
  </dl>
</main>
</body>
</html>
```